3 JPG Website Page Mockups need tidying / made into layered PSDs

Our website is aimed at creating a financial eduction site for females.

We have mockups of each page which are provided in jpeg.... but they need to be tidied up, layered into PSD (with descriptive layer names to allow coding from and no flattening - each object needs it's own layer) and we welcome any creative improvements suggested (although we are pretty happy with the way it's laid out at the moment as it is), without changing the feel, colour scheme or functionality of the site.

Three pages are needed:
Home page when not logged in
Home page when logged in
Topic header page

Please just upload the homepage to bid for the job... the winning designer will then have 5 days after they've been chosen to supply the psds of the other 2 pages .

I have also uploaded an image that can be used as a placeholder in the top box.
Thanks
Updates

As requested... Current font is Gill Sans MT

Thanks

Hi
Thanks for your designs.... For those of you still using the 4 circles (which I quite like), but haven't yet done so, could you see if you can move them around slightly to that the words don't get covered by the next circle?

Thanks

Reason: Designe has asked for An extension to work on new icons... would like to give them the time to see what they come up with, thanks

Industry/Entity Type

Financial

Requirements
Must have
• Maintain current feel & colour scheme of the website

```html
<!DOCTYPE html>
<html lang="en">
<head>
<meta charset="utf-8">
<title>Fairhaven Women – Home</title>
<link href="https://fonts.googleapis.com/css2?family=Cabin:wght@400;500;600;700&display=swap" rel="stylesheet">
<style>
:root{
  --teal:#12929a;
  --teal-dark:#0b7a83;
  --heading:#3f7f8e;
  --heading-dark:#2f6f7e;
  --text:#4a5a60;
  --link:#2f8a94;
  --orange:#f37a1f;
  --orange-light:#ffa24a;
  --sage:#8db48a;
  --sage-dark:#6f9a6c;
  --bg:#f3f5f5;
  --panel:#ffffff;
  --line:#b9c4c6;
  --header:#ececec;
}
*{box-sizing:border-box;margin:0;padding:0}
html,body{width:1200px;height:937px;overflow:hidden}
body{font-family:"Cabin",sans-serif;background:var(--bg);color:var(--text);position:relative}

/* top navigation */
.topnav{position:absolute;left:0;top:0;width:1200px;height:42px;background:linear-gradient(#1aa4aa,var(--teal-dark))}
.topnav .home-tab{position:absolute;left:142px;top:8px;width:48px;height:34px;background:var(--header);border-radius:4px 4px 0 0}
.topnav .home-tab svg{position:absolute;left:17px;top:7px}
.topnav a{position:absolute;top:13px;color:#fff;font-size:15px;text-decoration:none}
.topnav .locale{position:absolute;left:962px;top:15px;color:#fff;font-size:11px;display:flex;align-items:center;gap:4px}
.flag{width:18px;height:12px;background:#1b2a7a;display:inline-block}

/* header */
.header{position:absolute;left:0;top:42px;width:1200px;height:120px;background:var(--header);border-bottom:1px solid #dde}
.logo{position:absolute;left:142px;top:28px;font-size:48px;color:#111;letter-spacing:1px;font-weight:400}
.search-label{position:absolute;left:319px;top:15px;color:var(--link);font-size:15px}
.search{position:absolute;left:305px;top:38px;width:380px;height:34px;background:#fff;border:1px solid #ccd;border-radius:17px;font-size:13px;color:#666;padding:9px 0 0 15px}
.search .go{position:absolute;right:9px;top:7px}
.quick{position:absolute;top:84px;color:var(--link);font-size:12px;text-align:center}
.quick svg{display:block;margin:3px auto 0}
.pill{position:absolute;top:39px;height:31px;border:1px solid #d3d6d8;border-radius:16px;background:linear-gradient(#fff,#eee);font-size:11px;font-weight:700;color:#222;display:flex;align-items:center;gap:9px;padding-left:10px}
.dot{width:17px;height:17px;border-radius:50%;background:radial-gradient(circle at 40% 35%,#7fc0ff,#1a6fd8);display:flex;align-items:center;justify-content:center}

/* welcome line */
.welcome{position:absolute;left:144px;top:183px;color:var(--heading);font-size:20px}
.member{position:absolute;left:656px;top:187px;font-size:12px;color:#333;display:flex;gap:14px;align-items:center}
.member b{display:flex;align-items:center;gap:6px;font-size:13px}
.odot{width:16px;height:16px;border-radius:50%;background:var(--orange);color:#fff;font-size:11px;display:inline-flex;align-items:center;justify-content:center}

/* panels */
.panel{position:absolute;left:142px;width:869px;background:var(--panel);border:1px solid var(--line);border-radius:3px;overflow:hidden}

/* hero */
.hero{top:234px;height:228px}
.hero .photo{position:absolute;right:0;top:0;width:460px;height:228px;background:linear-gradient(90deg,#fff 0%,#efe4dc 25%,#d9b9a3 55%,#b88b70 100%)}
.hero h1{position:absolute;left:18px;top:14px;font-weight:400;font-size:28px;line-height:35px;color:var(--heading);white-space:nowrap}
.join{position:absolute;left:18px;top:150px;width:353px;height:61px;border-radius:31px;background:linear-gradient(#ffa451,var(--orange));color:#fff;font-size:27px;font-weight:700;display:flex;align-items:center;gap:14px;padding-left:18px}
.join .ring{width:34px;height:34px;border-radius:50%;background:#fff;display:flex;align-items:center;justify-content:center}
.member-card{position:absolute;left:731px;top:142px;width:122px;height:40px;background:rgba(255,255,255,.92);border-radius:4px;font-size:11px;color:#333;padding:5px 9px;line-height:14px;white-space:nowrap}
.member-card b{font-weight:600}
.pager{position:absolute;left:700px;top:191px;width:153px;height:24px;background:rgba(255,255,255,.92);border:1px solid #dde;font-size:11px;color:var(--sage-dark);display:flex;gap:9px;align-items:center;padding-left:5px}
.pager .cur{color:#333;text-decoration:underline}

/* topic feature */
.topic{top:513px;height:229px}
.video{position:absolute;left:51px;top:16px;width:256px;height:192px;background:linear-gradient(135deg,#5a3a2a,#8a6448 50%,#3a2a22);box-shadow:0 0 0 4px #fff,0 2px 6px rgba(0,0,0,.3)}
.video .play{position:absolute;left:105px;top:73px;width:46px;height:46px;background:rgba(0,0,0,.6)}
.video .caption{position:absolute;left:0;top:141px;width:153px;height:39px;background:rgba(120,175,125,.9);color:#fff;padding:3px 6px;font-size:14px;font-weight:600;letter-spacing:1px;line-height:15px}
.video .caption small{display:block;font-size:8px;letter-spacing:.5px;line-height:9px;font-weight:500}
.topic .eyebrow{position:absolute;left:372px;top:7px;font-size:20px;color:var(--heading)}
.topic h2{position:absolute;left:372px;top:31px;font-size:26px;line-height:38px;font-weight:700;color:var(--heading-dark);letter-spacing:.5px}
.more{position:absolute;left:372px;top:108px;font-size:13px;font-weight:700;color:var(--sage-dark)}

.circle{position:absolute;border-radius:50%;text-align:center}
.c-real{left:634px;top:66px;width:102px;height:102px;background:#fff;border:5px solid #efe8c8;padding:22px 0 0 12px;font-size:12px;font-weight:700;color:#333;line-height:16px;text-align:left}
.c-real span{font-size:9px;color:var(--sage-dark);font-weight:500}
.c-guide{left:443px;top:140px;width:86px;height:86px;background:#fff;border:5px solid #a9c7a6;padding-top:15px;font-size:12px;color:#333;line-height:14px}
.c-guide b{font-size:17px;display:block;line-height:17px}
.c-guide span{color:var(--sage-dark);font-size:10px}
.c-poll{left:527px;top:102px;width:112px;height:112px;background:linear-gradient(#e8f1f8,#d4e4ef);border:5px solid #fff;box-shadow:0 0 0 1px #cfdde3;padding-top:70px;font-size:13px;font-weight:700;color:#222}
.c-poll span{display:block;font-size:10px;font-weight:400;color:var(--link)}
.c-poll svg{position:absolute;left:13px;top:24px}
.c-ask{left:737px;top:88px;width:130px;height:130px;background:var(--sage);border:2px solid var(--sage-dark);color:#fff;font-size:11px;line-height:14px;padding:22px 12px 0}
.c-ask b{display:block;margin-top:4px;font-weight:500}

/* section icons */
.sections{position:absolute;left:142px;top:821px;width:880px;height:116px}
.tab{position:absolute;top:0;text-align:center;font-size:14px;color:var(--link)}
.tab .ico{width:56px;height:56px;margin:0 auto;border-radius:8px}
.tab p{margin-top:14px}
.tab.active{left:0;width:105px;height:116px;background:linear-gradient(#f08a4a,#f5b88e 45%,#f7f3ef);border-radius:6px 6px 0 0;color:#222;font-weight:600}
.tab.active svg{display:block;margin:8px auto 0}
.tab.active p{margin-top:6px}
</style>
</head>
<body>

<nav class="topnav">
  <div class="home-tab"><svg width="14" height="13" viewBox="0 0 14 13"><path d="M7 0 14 6H12V13H8V9H6V13H2V6H0Z" fill="#12929a"/></svg></div>
  <a style="left:204px">Polls</a>
  <a style="left:277px">Events</a>
  <a style="left:361px">Learning Center</a>
  <a style="left:510px">Find an Adviser</a>
  <a style="left:648px">Ask a Question</a>
  <a style="left:789px">About Us</a>
  <div class="locale"><span class="flag"></span>AU ▾</div>
</nav>

<header class="header">
  <div class="logo">LOGO</div>
  <div class="search-label">What are you looking for ?</div>
  <div class="search">Search Fairhaven Women for...
    <svg class="go" width="18" height="18" viewBox="0 0 18 18"><circle cx="9" cy="9" r="9" fill="#2a7fe0"/><circle cx="8" cy="8" r="3.5" fill="none" stroke="#fff" stroke-width="1.6"/><path d="M10.5 10.5 13 13" stroke="#fff" stroke-width="1.8"/></svg>
  </div>
  <div class="quick" style="left:313px">Popular Searches<svg width="10" height="7"><path d="M1 1 5 5 9 1" stroke="#2f8a94" stroke-width="2" fill="none"/></svg></div>
  <div class="quick" style="left:425px">Explore the Learning Center<svg width="10" height="7"><path d="M1 1 5 5 9 1" stroke="#2f8a94" stroke-width="2" fill="none"/></svg></div>
  <div class="quick" style="left:593px">Ask a Question<svg width="10" height="7"><path d="M1 1 5 5 9 1" stroke="#2f8a94" stroke-width="2" fill="none"/></svg></div>
  <div class="pill" style="left:749px;width:127px"><span class="dot"><svg width="7" height="8"><path d="M1 0 6 4 1 8" fill="#fff"/></svg></span>Find an Adviser</div>
  <div class="pill" style="left:885px;width:126px"><span class="dot"><svg width="7" height="8"><path d="M1 0 6 4 1 8" fill="#fff"/></svg></span>Contact Us</div>
</header>

<div class="welcome">Welcome to the new Fairhaven Women Site</div>
<div class="member">Already a member ?
  <b><span class="odot">+</span>Login</b>
  <b><span class="odot">›</span>Forgotten Password</b>
</div>

<section class="panel hero">
  <div class="photo" role="img" aria-label="Portrait photo of a smiling member"></div>
  <h1>We’re building Australia’s<br>biggest community dedicated to the<br>Financial Empowerment of Women.</h1>
  <div class="join"><span class="ring"><svg width="12" height="14"><path d="M2 1 10 7 2 13" stroke="#f37a1f" stroke-width="3" fill="none"/></svg></span>Join Now for FREE</div>
  <div class="member-card"><b>Maria</b><br>Member since 2006</div>
  <div class="pager">Previous <span>1</span><span>2</span><span>3</span><span class="cur">4</span> Next</div>
</section>

<section class="panel topic">
  <div class="video" role="img" aria-label="Video still of a guest speaker interview">
    <div class="play"><svg width="46" height="46"><path d="M18 14 32 23 18 32Z" fill="#fff"/></svg></div>
    <div class="caption">HELEN MARSH<small>FOUNDER, CHAIRMAN &amp; CEO<br>MARSH &amp; PARTNERS</small></div>
  </div>
  <div class="eyebrow">July Topic: Preparing for Retirement</div>
  <h2>Tommorow Can Belong to Those<br>Who Prepare Today</h2>
  <div class="more">Learn More ›</div>

  <div class="circle c-real">Real Women<br>Real Stories<br><span>See Video &gt;</span></div>
  <div class="circle c-guide">5 Minute<b>Guide</b><span>PDF &gt;</span></div>
  <div class="circle c-poll">
    <svg width="86" height="46" viewBox="0 0 86 46"><g fill="#7bb47a">
      <rect x="0" y="40" width="6" height="6" rx="2"/><rect x="9" y="36" width="6" height="10" rx="2"/><rect x="18" y="32" width="6" height="14" rx="2"/><rect x="27" y="26" width="6" height="20" rx="2"/><rect x="36" y="20" width="6" height="26" rx="2"/><rect x="45" y="12" width="6" height="34" rx="2"/><rect x="54" y="4" width="6" height="42" rx="2"/><rect x="63" y="8" width="6" height="38" rx="2"/><rect x="72" y="14" width="6" height="32" rx="2"/></g></svg>
    Take Our Poll<span>Vote &gt;</span>
  </div>
  <div class="circle c-ask">Have questions about Life States &amp; Planing? Ask a question or see what others have asked...<b>More ›</b></div>
</section>

<div class="sections">
  <div class="tab active">
    <svg width="44" height="44" viewBox="0 0 44 44"><circle cx="22" cy="13" r="9" fill="#fff"/><path d="M4 44C4 30 12 24 22 24S40 30 40 44Z" fill="#fff"/></svg>
    <p>Welcome</p>
  </div>
  <div class="tab" style="left:121px;width:80px"><div class="ico" role="img" aria-label="Events icon" style="background:#b0174f"></div><p>Events</p></div>
  <div class="tab" style="left:228px;width:84px"><div class="ico" role="img" aria-label="Webcasts icon" style="background:#8c8c8c;border-radius:50%"></div><p>Webcasts</p></div>
  <div class="tab" style="left:336px;width:80px"><div class="ico" role="img" aria-label="My Family icon" style="background:linear-gradient(#d8262a 45%,#e6e0d6 45%)"></div><p>My Family</p></div>
  <div class="tab" style="left:437px;width:102px"><div class="ico" role="img" aria-label="My Investments icon" style="background:#e6e6ea"></div><p>My Investments</p></div>
  <div class="tab" style="left:553px;width:102px"><div class="ico" role="img" aria-label="My Retirement icon" style="background:linear-gradient(135deg,#2a6fd0,#e8efe6)"></div><p>My Retirement</p></div>
  <div class="tab" style="left:667px;width:76px"><div class="ico" role="img" aria-label="My Estate icon" style="background:#2aa9b5"></div><p>My Estate</p></div>
  <div class="tab" style="left:764px;width:88px"><div class="ico" role="img" aria-label="My Lifestyle icon" style="background:radial-gradient(#7fcf5a,#2f8a2c);border-radius:50%"></div><p>My Lifestyle</p></div>
</div>

</body>
</html>
```